Beautiful Quotes For Social Media Posts

We are looking for 5 beautifully designed quotes for our social media account.

Inspiration of styles we like in both style and color along with a few of our favorite fonts (you are NOT limited to these fonts this is just to give you an idea):
https://quillmorestudio.example.com/s/k7p2vx9tqa41mzn8wbd3ce6hr5lf0y2j

*These fonts are property of Quillmore Studio. You do not have permission/rights to use them outside of this assignment*

Quotes to use (5):
“Only those who dare to fail greatly can ever achieve greatly.” –Vernon T. Ashgrove
“Don’t go through life, grow through life.” – Milo Pendrake
“Follow your bliss and the universe will open doors where there were only walls.” – Arthur Venholm
“If you don’t like the road you’re walking, start paving another one.” – Greta Mossley
“Life is like riding a bicycle. To keep your balance, you must keep moving.” —Lucian Thornwick

File Specifics:
- JPG
- 10x10 in size (square)
- Please include @QuillmoreStudio in the bottom right left or center of each design

Brand Details:
Soft but rich pastel and bright colors.
Hand Drawn florals, doodles and art
Handwritten looking fonts
Artsy, Creative, Girl and Inspiring

```html
<!DOCTYPE html>
<html lang="en">
<head>
<meta charset="utf-8">
<title>Quote Posts – Quillmore Studio</title>
<link rel="stylesheet" href="https://fonts.googleapis.com/css2?family=Amatic+SC:wght@700&family=Righteous&family=Kaushan+Script&family=Montserrat:ital,wght@0,400;0,600;0,800;0,900;1,800;1,900&family=Sacramento&family=Oswald:wght@500;600&family=Libre+Baskerville&display=swap">
<style>
  :root {
    --coral: #fd9184;
    --coral-line: rgba(255,255,255,0.12);
    --coral-floral: #fda095;
    --tangerine: #fe8c55;
    --tangerine-pattern: #fe9762;
    --lime: #e8e54f;
    --mint: #a5e57a;
    --aqua: #54e0c4;
    --teal: #26d8bc;
    --rose: #fe5a82;
    --rose-floral: #fe6d90;
    --pumpkin: #e97432;
    --ice: #bfe6f2;
    --white: #ffffff;
    --shadow: rgba(120,40,30,0.35);
  }
  * { margin: 0; padding: 0; box-sizing: border-box; }
  html, body { width: 1200px; height: 783px; overflow: hidden; background: var(--white); }
  .board { position: relative; width: 1200px; height: 783px; }
  .post { position: absolute; overflow: hidden; color: var(--white); text-align: center; }
  .post--r1 { top: 0; height: 400px; }
  .post--r2 { top: 400px; height: 383px; }
  .post--c1 { left: 0; width: 400px; }
  .post--c2 { left: 400px; width: 400px; }
  .post--c3 { left: 800px; width: 400px; }
  .line { position: absolute; left: 0; right: 0; white-space: nowrap; }
  .handle { font-family: "Libre Baskerville", serif; font-size: 14px; }
  .floral { position: absolute; border-radius: 50%; }

  /* Post 1 – dare */
  .dare { background: var(--coral) repeating-linear-gradient(to bottom, transparent 0 27px, var(--coral-line) 27px 28px); }
  .dare .floral { background: var(--coral-floral); width: 64px; height: 64px; }
  .dare__quote { font-family: "Amatic SC", sans-serif; font-size: 42px; text-shadow: 2px 2px 2px var(--shadow); line-height: 1; }
  .dare__accent { color: var(--ice); text-decoration: underline; text-decoration-thickness: 3px; text-underline-offset: 4px; }
  .dare__author { font-family: "Oswald", sans-serif; font-size: 13px; font-weight: 500; }

  /* Post 2 – bliss */
  .bliss { background: radial-gradient(ellipse at 30% 40%, var(--tangerine-pattern), var(--tangerine) 60%); }
  .bliss__small { font-family: "Montserrat", sans-serif; font-size: 8px; letter-spacing: 3px; font-weight: 600; }
  .bliss__caps { font-family: "Righteous", sans-serif; line-height: 1; }
  .bliss__script { font-family: "Kaushan Script", cursive; font-size: 40px; line-height: 1; }
  .bliss__follow { font-family: "Montserrat", sans-serif; font-size: 12px; letter-spacing: 5px; font-weight: 600; }

  /* Post 3 – bicycle */
  .bicycle { background: linear-gradient(35deg, var(--lime) 0%, var(--mint) 50%, var(--aqua) 100%); }
  .bicycle .floral { background: rgba(255,255,255,0.25); width: 50px; height: 80px; }
  .bicycle__script { font-family: "Sacramento", cursive; line-height: 1; white-space: nowrap; }
  .bicycle__caps { font-family: "Oswald", sans-serif; font-weight: 600; letter-spacing: -0.5px; line-height: 1; white-space: nowrap; }
  .bicycle__sans { font-family: "Montserrat", sans-serif; line-height: 1; white-space: nowrap; }

  /* Post 4 – grow */
  .grow { background: var(--teal); }
  .grow__quote { position: absolute; left: 108px; top: 80px; text-align: left; font-family: "Montserrat", sans-serif; font-weight: 900; font-style: italic; font-size: 30px; line-height: 37px; color: var(--coral); -webkit-text-stroke: 1px var(--white); text-shadow: 2px 2px 0 var(--white); letter-spacing: -0.5px; white-space: nowrap; }
  .grow__mark { position: absolute; left: -24px; top: -4px; color: var(--white); -webkit-text-stroke: 0; text-shadow: none; font-family: "Libre Baskerville", serif; font-style: normal; }
  .grow__author { position: absolute; right: 88px; top: 266px; font-family: "Montserrat", sans-serif; font-style: italic; font-weight: 800; font-size: 10px; color: var(--white); }

  /* Post 5 – road */
  .road { background: var(--rose) repeating-linear-gradient(to bottom, transparent 0 27px, rgba(255,255,255,0.08) 27px 28px); }
  .road .floral { background: var(--rose-floral); width: 66px; height: 66px; }
  .road__stack { position: absolute; left: 109px; top: 44px; width: 180px; font-family: "Montserrat", sans-serif; font-weight: 900; line-height: 0.8; text-shadow: 2px 3px 3px rgba(120,20,50,0.45); text-align: left; }
  .road__row { display: flex; align-items: flex-end; white-space: nowrap; }
  .road__side { writing-mode: vertical-rl; transform: rotate(180deg); font-size: 10px; line-height: 1; margin-right: 2px; }
  .road__author { font-family: "Montserrat", sans-serif; font-weight: 800; font-size: 10px; letter-spacing: 1px; }

  /* Post 6 – studio name */
  .studio { background: var(--pumpkin); text-align: left; }
  .studio__name { position: absolute; left: 90px; top: 100px; font-family: "Libre Baskerville", serif; font-size: 54px; line-height: 89px; white-space: nowrap; }
</style>
</head>
<body>
<main class="board">

  <section class="post post--r1 post--c1 dare">
    <div class="floral" style="left:-8px;top:-10px" role="img" aria-label="Hand drawn flower outline"></div>
    <div class="floral" style="right:-8px;top:-10px" role="img" aria-label="Hand drawn flower outline"></div>
    <div class="floral" style="left:-4px;top:290px" role="img" aria-label="Hand drawn floral sprig"></div>
    <div class="floral" style="right:-4px;top:290px" role="img" aria-label="Hand drawn floral sprig"></div>
    <p class="line dare__quote" style="top:96px">Only those who dare who</p>
    <p class="line dare__quote" style="top:153px">dare to <span class="dare__accent">fail greatly</span></p>
    <p class="line dare__quote" style="top:211px">can ever <span class="dare__accent">achieve greatly.</span></p>
    <p class="line dare__author" style="top:290px">— VERNON T. ASHGROVE —</p>
    <p class="line handle" style="top:362px">@QuillmoreStudio</p>
  </section>

  <section class="post post--r1 post--c2 bliss">
    <div style="position:absolute;inset:0;opacity:0.5;background:var(--tangerine-pattern)" role="img" aria-label="Faint topographic line pattern"></div>
    <p class="line bliss__follow" style="top:44px">FOLLOW</p>
    <p class="line bliss__small" style="top:61px">YOUR</p>
    <p class="line bliss__caps" style="top:76px;font-size:40px">Bliss</p>
    <p class="line bliss__small" style="top:122px">AND THE</p>
    <p class="line bliss__script" style="top:128px">Universe</p>
    <p class="line bliss__small" style="top:180px">WILL</p>
    <p class="line bliss__caps" style="top:190px;font-size:44px">Open Doors</p>
    <p class="line bliss__small" style="top:237px">WHERE THERE WERE</p>
    <p class="line bliss__small" style="top:260px">ONLY</p>
    <p class="line bliss__script" style="top:270px">Walls.</p>
    <p class="line bliss__small" style="top:341px">-ARTHUR VENHOLM-</p>
    <p class="line handle" style="top:372px">@QuillmoreStudio</p>
  </section>

  <section class="post post--r1 post--c3 bicycle">
    <div class="floral" style="left:-10px;top:14px" role="img" aria-label="Hand drawn floral sprig"></div>
    <div class="floral" style="right:-10px;top:270px" role="img" aria-label="Hand drawn floral sprig"></div>
    <p class="bicycle__script" style="position:absolute;left:74px;top:66px;font-size:74px">Life</p>
    <p class="bicycle__sans" style="position:absolute;left:168px;top:84px;font-size:17px">is like riding a</p>
    <p class="bicycle__caps" style="position:absolute;left:168px;top:106px;font-size:42px">BICYCLE.</p>
    <p class="bicycle__sans" style="position:absolute;left:80px;top:164px;font-size:17px">To keep you <span class="bicycle__script" style="font-size:32px;vertical-align:-4px">balance</span></p>
    <p class="bicycle__caps" style="position:absolute;left:78px;top:190px;font-size:40px">YOU MUST KEEP,</p>
    <p class="bicycle__script" style="position:absolute;left:92px;top:228px;font-size:80px">Moving</p>
    <p class="line bicycle__sans" style="top:320px;font-size:11px;font-weight:600">-LUCIAN THORNWICK-</p>
    <p class="line handle" style="top:362px">@QuillmoreStudio</p>
  </section>

  <section class="post post--r2 post--c1 grow">
    <svg width="400" height="383" style="position:absolute;left:0;top:0" aria-hidden="true">
      <g fill="var(--rose)">
        <circle cx="362" cy="32" r="81"/>
        <circle cx="0" cy="94" r="58"/>
        <circle cx="46" cy="356" r="62"/>
        <circle cx="378" cy="341" r="85"/>
      </g>
      <g fill="none" stroke="var(--white)" stroke-width="3" stroke-linecap="round" stroke-dasharray="0 9">
        <circle cx="362" cy="32" r="100"/>
        <circle cx="0" cy="94" r="76"/>
        <circle cx="46" cy="356" r="82"/>
        <circle cx="378" cy="341" r="104"/>
      </g>
    </svg>
    <div class="grow__quote">
      <span class="grow__mark">“</span>
      DON’T GO<br>THROUGH<br>LIFE, GROW<br>THROUGH<br>LIFE. <span class="grow__mark" style="position:static">”</span>
    </div>
    <p class="grow__author">-MILO PENDRAKE</p>
    <p class="line handle" style="top:353px">@QuillmoreStudio</p>
  </section>

  <section class="post post--r2 post--c2 road">
    <div class="floral" style="left:-6px;top:-10px" role="img" aria-label="Hand drawn flower outline"></div>
    <div class="floral" style="right:-6px;top:-10px" role="img" aria-label="Hand drawn flower outline"></div>
    <div class="floral" style="left:-6px;top:280px" role="img" aria-label="Hand drawn floral sprig"></div>
    <div class="floral" style="right:-6px;top:280px" role="img" aria-label="Hand drawn floral sprig"></div>
    <div class="road__stack">
      <div class="road__row" style="font-size:56px"><span class="road__side">IF</span>YOU</div>
      <div class="road__row" style="font-size:44px">DON’T</div>
      <div class="road__row" style="font-size:30px">LIKE THE</div>
      <div class="road__row" style="font-size:48px">ROAD</div>
      <div class="road__row" style="font-size:28px"><span class="road__side" style="font-size:8px">YOU’RE</span>WALKING</div>
      <div class="road__row" style="font-size:44px">START</div>
      <div class="road__row" style="font-size:38px">PAVING</div>
      <div class="road__row" style="font-size:18px">ANOTHER ONE.</div>
    </div>
    <p class="line road__author" style="top:323px">- GRETA MOSSLEY -</p>
    <p class="line handle" style="top:357px">@QuillmoreStudio</p>
  </section>

  <section class="post post--r2 post--c3 studio">
    <p class="studio__name">Quillmore<br>Studio</p>
  </section>

</main>
</body>
</html>
```